REDESIGN COUPLE PAGES FOR SURGE VIDEO ADS

PLEASE REDESIGN THIS PAGE FOR ME:
http://pagekitfinder.com/rk/milo/surge/pricing.html
I need it to be easy to read for the end user so the customer knows exactly what he will be getting. Make an emphasis on the subscription as the most popular item....and also the price per video format should be emphasized too.

Target Market(s)

B2B

Industry/Entity Type

Video Production

Number of Pages Required

3 page

Colors

Designer to choose colors to be used in the design.

Requirements
Must have
• PLEASE REDESIGN THIS PAGE FOR ME:
• http://pagekitfinder.com/rk/milo/surge/pricing.html
• I need it to be easy to read for the end user so the customer knows exactly what he will be getting. Make an emphasis on the subscription as the most popular item....and also the price per video format should be emphasized too.
Nice to have
Should not have

```html
<!DOCTYPE html>
<html lang="en">
<head>
<meta charset="utf-8">
<title>SURGE – Pricing</title>
<link href="https://fonts.googleapis.com/css2?family=Open+Sans:wght@400;600;700&family=Roboto:wght@700;900&display=swap" rel="stylesheet">
<style>
:root{
  --navy:#121c2d;
  --white:#ffffff;
  --ink:#1b1b1b;
  --muted:#444;
  --head-grey:#ececec;
  --line:#d6d6d6;
  --blue:#3c89e0;
  --blue-light:#5ec6f4;
  --btn-a:#2e62d8;
  --btn-b:#3b8ee8;
  --nav-active:#4aa7e8;
}
*{box-sizing:border-box;margin:0;padding:0}
html,body{width:1200px;height:1148px;overflow:hidden;background:var(--white);font-family:"Open Sans",Arial,sans-serif;color:var(--ink)}
.page{position:relative;width:1200px;height:1148px}

.topbar{position:absolute;left:0;top:0;width:1200px;height:48px;background:var(--navy)}
.brand{position:absolute;left:173px;top:9px;color:var(--white)}
.brand-name{font-weight:700;font-size:17px;letter-spacing:2px;line-height:18px;display:flex;align-items:center;gap:6px}
.brand-mark{width:10px;height:10px;background:var(--blue-light)}
.brand-tag{font-size:6px;font-weight:600;letter-spacing:.5px;color:#c9ced8;margin-top:2px}
.nav{position:absolute;left:436px;top:18px;display:flex;gap:15px;font-size:10px;font-weight:600;color:var(--white)}
.nav .active{color:var(--nav-active)}
.login{position:absolute;left:939px;top:19px;font-size:9.5px;font-weight:600;color:var(--white)}
.signup{position:absolute;left:978px;top:12px;width:51px;height:25px;background:var(--blue);color:var(--white);font-size:9.5px;font-weight:600;display:flex;align-items:center;justify-content:center;border-radius:2px}

.title{position:absolute;left:0;top:83px;width:1200px;text-align:center;font-family:"Roboto",Arial,sans-serif;font-weight:900;font-size:23.5px;letter-spacing:-.2px}

.plans{position:absolute;left:172px;top:145px;display:flex;gap:5px}
.plan{width:167px;height:483px;background:var(--white);box-shadow:0 1px 4px rgba(0,0,0,.2);position:relative;text-align:center}
.plan-head{height:61px;background:var(--head-grey);padding-top:14px}
.plan-name{font-size:12px;font-weight:700;letter-spacing:.3px}
.plan-sub{font-size:7.5px;font-weight:700;margin-top:6px}
.price{position:relative;height:79px}
.starts{position:absolute;left:0;width:100%;top:7px;font-size:6.5px}
.price-row{position:absolute;left:0;width:100%;top:20px;display:flex;justify-content:center;align-items:flex-start;gap:4px}
.cur{font-size:15px;margin-top:15px}
.amount{font-size:45px;line-height:48px;font-weight:400;letter-spacing:-1px}
.per{font-size:6.5px;line-height:9px;text-align:left;margin-top:13px;margin-left:4px}
.features{list-style:none;margin:0 17px}
.features li{height:28px;line-height:28px;font-size:11px;color:var(--muted);border-bottom:1px solid var(--line)}
.block{margin:0 17px;height:89px;border-bottom:1px solid var(--line);padding-top:9px}
.block-title{font-size:7.5px;font-weight:700;margin-bottom:8px}
.block-text{font-size:9px;line-height:12.3px;color:var(--ink)}
.block-text.centered{padding-top:8px}
.themes{margin:0 17px;padding-top:10px}
.buy{position:absolute;left:17px;bottom:18px;width:132px;height:35px;background:linear-gradient(90deg,var(--btn-a),var(--btn-b));color:var(--white);font-weight:700;font-size:14px;display:flex;align-items:center;justify-content:center;border-radius:2px}

.plan.featured{background:var(--blue);color:#d9ecff;box-shadow:none}
.plan.featured .plan-head{background:var(--blue-light);color:var(--white)}
.plan.featured .features li{color:#e4f1ff;border-color:#8fbcf0}
.plan.featured .block{border-color:#8fbcf0}
.plan.featured .block-text,.plan.featured .block-title{color:#e4f1ff}
.plan.featured .amount,.plan.featured .cur{color:var(--white)}
.plan.featured .buy{background:var(--white);color:var(--btn-a)}

.included{position:absolute;left:0;top:678px;width:1200px;text-align:center}
.included h2{font-size:12.5px;font-weight:700}
.included p{font-size:11px;line-height:14px;margin-top:11px}

.footer{position:absolute;left:0;top:934px;width:1200px;height:214px;background:var(--navy);color:var(--white)}
.foot-brand{position:absolute;left:254px;top:54px}
.foot-brand .brand-name{font-size:28px;letter-spacing:4px;line-height:30px;gap:8px}
.foot-brand .brand-mark{width:14px;height:14px}
.foot-brand .brand-tag{font-size:10px;letter-spacing:1px;margin-top:1px}
.foot-slogan{position:absolute;left:254px;top:105px;font-size:12px;font-weight:700;letter-spacing:-.3px}
.col-title{font-size:12px;margin-bottom:15px;position:relative}
.col-title::after{content:"";position:absolute;left:0;bottom:-7px;width:16px;height:1px;background:#6b7487}
.links{position:absolute;left:551px;top:55px}
.links a{display:block;font-size:9.5px;color:var(--white);text-decoration:none;line-height:21px}
.about{position:absolute;left:729px;top:55px;width:220px}
.about p{font-size:10.5px;line-height:16px;margin-top:17px}
.social{display:flex;gap:8px;margin-top:12px}
.social span{width:24px;height:24px;border-radius:50%;background:#263246}
</style>
</head>
<body>
<div class="page">
  <header class="topbar">
    <div class="brand">
      <div class="brand-name"><span class="brand-mark"></span>SURGE</div>
      <div class="brand-tag">MARKETING VIDEOS MADE FOR YOU</div>
    </div>
    <nav class="nav">
      <span>Home</span><span>How It Works</span><span>Examples</span><span>FAQ</span><span>Contact Us</span><span class="active">Pricing</span><span>Calendar</span>
    </nav>
    <span class="login">Log In</span>
    <span class="signup">Sign Up</span>
  </header>

  <h1 class="title">CHOOSE THE BEST VIDEO OPTION FOR YOU!</h1>

  <section class="plans">
    <article class="plan">
      <div class="plan-head"><div class="plan-name">AL A CARTE</div><div class="plan-sub">As needed basis</div></div>
      <div class="price"><div class="starts">Starts at</div><div class="price-row"><span class="cur">$</span><span class="amount">37</span></div></div>
      <ul class="features"><li>Quantity: Custom</li><li>24 hours to delivery</li><li>Unlimited Revisions</li><li>MP4 FULL HD 1080P</li></ul>
      <div class="block"><div class="block-title">VIDEO FORMATS</div><div class="block-text">Wide screen video format<br>Large square video format<br>Vertical video format<br>Page cover video format</div></div>
      <div class="themes"><div class="block-title">THEMES</div><div class="block-text">Holiday (optional)<br>Seasonal (optional)</div></div>
      <span class="buy">BUY NOW</span>
    </article>

    <article class="plan featured">
      <div class="plan-head"><div class="plan-name">SUBSCRIPTION</div><div class="plan-sub">New video ads monthly</div></div>
      <div class="price"><div class="starts">Starts at</div><div class="price-row"><span class="cur">$</span><span class="amount">16</span><span class="per">per<br>video</span></div></div>
      <ul class="features"><li>Quantity: Custom</li><li>24 hours to delivery</li><li>Unlimited Revisions</li><li>MP4 FULL HD 1080P</li></ul>
      <div class="block"><div class="block-title">VIDEO FORMATS</div><div class="block-text">Wide screen video format<br>Large square video format<br>Vertical video format<br>Page cover video format</div></div>
      <div class="themes"><div class="block-title">THEMES</div><div class="block-text">Holiday<br>Seasonal</div></div>
      <span class="buy">BUY NOW</span>
    </article>

    <article class="plan">
      <div class="plan-head"><div class="plan-name">HOLIDAY PKG</div><div class="plan-sub">17 Holiday themed videos</div></div>
      <div class="price"><div class="price-row"><span class="cur">$</span><span class="amount">14</span><span class="per">per<br>video</span></div></div>
      <ul class="features"><li>Quantity: 17 videos</li><li>3-5 days to delivery</li><li>Unlimited Revisions</li><li>MP4 FULL HD 1080P</li></ul>
      <div class="block"><div class="block-title">VIDEO FORMATS</div><div class="block-text">Wide screen video format<br>Large square video format<br>Vertical video format<br>Page cover video format</div></div>
      <div class="themes"><div class="block-title">THEMES</div><div class="block-text">Holiday</div></div>
      <span class="buy">BUY NOW</span>
    </article>

    <article class="plan">
      <div class="plan-head"><div class="plan-name">SEASON PKG</div><div class="plan-sub">4 seasonal themed videos</div></div>
      <div class="price"><div class="price-row"><span class="amount">18</span></div></div>
      <ul class="features"><li>Quantity: 4 videos</li><li>3-5 days to delivery</li><li>Unlimited Revisions</li><li>MP4 FULL HD 1080P</li></ul>
      <div class="block"><div class="block-title">VIDEO FORMATS</div><div class="block-text">Wide screen video format<br>Large square video format<br>Vertical video format<br>Page cover video format</div></div>
      <div class="themes"><div class="block-title">THEMES</div><div class="block-text">Seasonal</div></div>
      <span class="buy">BUY NOW</span>
    </article>

    <article class="plan">
      <div class="plan-head"><div class="plan-name">SOCIAL MEDIA</div><div class="plan-sub">Daily videos for your social media</div></div>
      <div class="price"><div class="price-row"><span class="amount">10</span><span class="per">per<br>video</span></div></div>
      <ul class="features"><li>Quantity: 30 videos</li><li>Prior to next month</li><li>Unlimited Revisions</li><li>MP4 FULL HD 1080P</li></ul>
      <div class="block"><div class="block-title">VIDEO FORMATS</div><div class="block-text centered"><br>Large square video format</div></div>
      <div class="themes"><div class="block-title">THEMES</div><div class="block-text">Holiday<br>Seasonal</div></div>
      <span class="buy">BUY NOW</span>
    </article>
  </section>

  <section class="included">
    <h2>YOUR VIDEOS WITH CONTENT DONE FOR YOU</h2>
    <p>Full branding in video; Full copyright ownership; Full reselling rights; Premium video clips;<br>Use my images; Use my video footage; Use my background music; Fully licensed background music</p>
  </section>

  <footer class="footer">
    <div class="foot-brand">
      <div class="brand-name"><span class="brand-mark"></span>SURGE</div>
      <div class="brand-tag">MARKETING VIDEOS MADE FOR YOU</div>
    </div>
    <div class="foot-slogan">CREATED BY A MARKETER FOR MARKETERS.</div>
    <div class="links">
      <div class="col-title">Quick Links</div>
      <a href="#">How It Works</a><a href="#">Term Of Service</a><a href="#">Privacy Policy</a><a href="#">Cookies Policy</a>
    </div>
    <div class="about">
      <div class="col-title">About Us</div>
      <p>With Surge, you simply let us know what you want to promote and we will have your video ad finished as soon as 24 hours!</p>
      <div class="social"><span></span><span></span><span></span><span></span><span></span></div>
    </div>
  </footer>
</div>
</body>
</html>
```